Silver Fern Counseling business cards

Dana Korvath, LCPC, NCC
(410)555-0187
www.silverferncounseling.example
dana@silverferncounseling.example

Business cards. I would like it on the same background as pictured. Not on a white business card. I have attached the logo that was done by another designer with artflockly. I am open to looking at single-sided and double-sided designs.

Target Market(s)

teenagers and adults

Industry/Entity Type

mental health

Contact Information for Business Card

Dana Korvath, LCPC, NCC (410)555-0187 dana@silverferncounseling.example

Font styles to use
Other font styles liked:
• Cinzel

Colors

Designer to choose colors to be used in the design.

Requirements
Must have
• logo that is attached

```html
<!DOCTYPE html>
<html lang="en">
<head>
<meta charset="utf-8">
<title>Silver Fern Counseling — Business Cards</title>
<link rel="stylesheet" href="https://fonts.googleapis.com/css2?family=Montserrat:wght@400;500;700&display=swap">
<style>
  :root {
    --page-bg: #3a3a3c;
    --card-white: #ffffff;
    --navy: #124a6e;
    --navy-band: #245b80;
    --teal: #4fb0aa;
    --green: #7d9e57;
    --coral: #e0826a;
    --grey-text: #4a4a4a;
    --back-dark: #0f2633;
    --back-mid: #2f4d5a;
    --logo-light: #8fd3dc;
  }
  * { box-sizing: border-box; margin: 0; padding: 0; }
  html, body {
    width: 1200px; height: 1200px; overflow: hidden;
    background: var(--page-bg);
    font-family: "Montserrat", sans-serif;
  }
  .sheet {
    position: relative; width: 1200px; height: 1200px;
    display: flex; flex-direction: column; align-items: center;
    justify-content: center; gap: 44px;
  }
  .card {
    position: relative; width: 900px; height: 514px;
    border-radius: 36px; overflow: hidden;
    box-shadow: 0 18px 40px rgba(0,0,0,.45);
  }
  /* Front */
  .card-front { background: var(--card-white); }
  .front-brand {
    position: absolute; top: 70px; right: 70px;
    display: flex; align-items: center; gap: 16px;
  }
  .brand-dot {
    width: 40px; height: 40px; border-radius: 50%;
    background: var(--teal);
  }
  .brand-name {
    font-weight: 700; font-size: 30px; color: var(--navy);
    letter-spacing: .5px;
  }
  .contact-block {
    position: absolute; left: 70px; bottom: 80px;
  }
  .person-name {
    font-weight: 700; font-size: 54px; color: var(--navy);
    text-transform: uppercase; letter-spacing: 1px; line-height: 1;
  }
  .person-credentials {
    font-weight: 400; font-size: 26px; color: var(--grey-text);
    margin: 8px 0 22px;
  }
  .contact-line {
    display: flex; align-items: center; gap: 16px;
    font-size: 26px; color: var(--grey-text); margin-top: 8px;
  }
  .contact-icon { width: 30px; height: 30px; flex: none; }
  .color-band {
    position: absolute; left: 0; right: 0; bottom: 0; height: 26px;
    display: flex;
  }
  .band-navy  { width: 36%; background: var(--navy-band); }
  .band-teal  { width: 20%; background: var(--teal); }
  .band-green { width: 26%; background: var(--green); }
  .band-coral { width: 18%; background: var(--coral); }
  /* Back */
  .card-back {
    background: radial-gradient(ellipse at 55% 40%, var(--back-mid) 0%, var(--back-dark) 80%);
    display: flex; align-items: center; justify-content: center;
  }
  .back-brand { display: flex; align-items: center; gap: 22px; }
  .back-brand .brand-dot { width: 60px; height: 60px; background: var(--logo-light); }
  .back-brand .brand-name { font-size: 48px; color: var(--logo-light); }
</style>
</head>
<body>
<main class="sheet">
  <section class="card card-front">
    <div class="front-brand">
      <span class="brand-dot"></span>
      <span class="brand-name">Silver Fern Counseling</span>
    </div>
    <div class="contact-block">
      <h1 class="person-name">Dana Korvath</h1>
      <p class="person-credentials">LCPC | NCC</p>
      <p class="contact-line">
        <svg class="contact-icon" viewBox="0 0 24 24" aria-hidden="true">
          <path fill="#124a6e" d="M6.6 10.8a15.1 15.1 0 0 0 6.6 6.6l2.2-2.2a1 1 0 0 1 1-.25 11.4 11.4 0 0 0 3.6.57 1 1 0 0 1 1 1V20a1 1 0 0 1-1 1A17 17 0 0 1 3 4a1 1 0 0 1 1-1h3.5a1 1 0 0 1 1 1c0 1.25.2 2.45.57 3.57a1 1 0 0 1-.25 1z"/>
        </svg>
        (410)555-0187
      </p>
      <p class="contact-line">
        <svg class="contact-icon" viewBox="0 0 24 24" aria-hidden="true">
          <rect x="2" y="5" width="20" height="14" fill="#124a6e"/>
          <path d="M2 5l10 8 10-8M2 19l7-7M22 19l-7-7" fill="none" stroke="#ffffff" stroke-width="1.6"/>
        </svg>
        dana@silverferncounseling.example
      </p>
    </div>
    <div class="color-band">
      <span class="band-navy"></span><span class="band-teal"></span>
      <span class="band-green"></span><span class="band-coral"></span>
    </div>
  </section>

  <section class="card card-back">
    <div class="back-brand">
      <span class="brand-dot"></span>
      <span class="brand-name">Silver Fern Counseling</span>
    </div>
  </section>
</main>
</body>
</html>
```